Website Design for a holiday home letting busines

We require a redesign of our present website www.birchwoodstays.com. We want the website to stand out and look professional and clean to make holiday hunters want to book a caravan or lodge holiday with us. Our logo is red however we DO NOT want the website to be red. We want a natural colour scheme.

The final design should communicate that we are a professional company to book with.

On the home page we require;
Overview of company
Photo
Search box for holiday (check in)
Late Deals
Reviews
News

We would like the following pages designed; home page, available dates page, caravans page, content page.

The website should be responsive for smart phones. One website I do like is http://www.verdamoro.be/nl/

Target Market(s)

Families

Industry/Entity Type

Travel

Number of Pages Required

5+ page

Font styles to use
Serif

Requirements
Must have
• The project must be responsive for mobile phones and tablets.
• Ability to search for holiday home holidays
• We want a natural colour scheme.
Nice to have
• A style we like is http://www.verdamoro.be/nl/
Should not have
• Do not use red as a colour for the website. Our logo is red so this is the only time we want this used.

```html
<!DOCTYPE html>
<html lang="en">
<head>
<meta charset="utf-8">
<title>Birchwood Stays – Lodge &amp; Caravan Holidays</title>
<link href="https://fonts.googleapis.com/css2?family=Lora:wght@400;500;600;700&display=swap" rel="stylesheet">
<style>
:root{
  --ink:#333333;
  --muted:#777777;
  --line:#dddddd;
  --nav:#3b3b3b;
  --nav-dark:#2e2e2e;
  --logo:#c8161d;
  --moss:#5b7a3a;
  --moss-dark:#4a6530;
  --earth:#4a3325;
  --earth-soft:rgba(58,38,26,.88);
  --footer:#2a2a2a;
  --footer-deep:#1f1f1f;
  --paper:#ffffff;
  --sky:#6fb4d8;
  --sea:#2e8fb3;
  --sand:#e9dcc2;
}
*{box-sizing:border-box;margin:0;padding:0}
html,body{width:1200px;height:2816px;overflow:hidden;background:var(--paper);font-family:"Lora",Georgia,serif;color:var(--ink)}
.page{position:relative;width:1200px;height:2816px}
.wrap{width:980px;margin:0 auto;position:relative}

/* header */
.site-header{height:120px;background:var(--paper)}
.site-header .wrap{height:120px;display:flex;align-items:center;justify-content:space-between}
.brand{display:flex;align-items:center;gap:12px}
.brand-dot{width:40px;height:40px;border-radius:50%;background:var(--logo)}
.brand-name{font-size:22px;font-weight:700;color:var(--logo)}
.header-right{display:flex;flex-direction:column;align-items:flex-end;gap:12px}
.contact-line{display:flex;gap:22px;font-size:12px;color:var(--muted);align-items:center}
.contact-line span{display:flex;align-items:center;gap:6px}
.socials{display:flex;gap:6px}
.socials i{display:block;width:22px;height:22px;background:var(--nav)}
.header-tools{display:flex;gap:14px;align-items:center}
.site-search{display:flex}
.site-search input{width:170px;height:24px;border:1px solid var(--line);font:12px "Lora",Georgia,serif;padding:0 8px;color:var(--muted)}
.site-search button{height:24px;padding:0 12px;background:var(--moss);color:#fff;border:0;font:600 11px "Lora",Georgia,serif}

/* nav */
.main-nav{height:64px;background:var(--nav);border-bottom:4px solid var(--nav-dark)}
.main-nav ul{list-style:none;display:flex;height:60px;width:980px;margin:0 auto}
.main-nav li{display:flex;align-items:center;padding:0 16px;font-size:12.5px;font-weight:600;color:#eee;text-transform:uppercase;border-right:1px solid #4a4a4a;white-space:nowrap}
.main-nav li.active{background:var(--moss)}

/* hero */
.hero{position:relative;height:636px}
.hero-photo{position:absolute;inset:0;background:linear-gradient(180deg,var(--sky) 0%,#a9d6ec 40%,var(--sea) 62%,#5fb0c9 72%,var(--sand) 86%,#d9c9a8 100%)}
.hero-copy{position:absolute;left:150px;top:110px;color:#fff}
.hero-copy h1{font-size:44px;line-height:1.18;font-weight:700}
.hero-copy p{margin-top:16px;font-size:15px;line-height:1.5;width:340px}
.booking{position:absolute;left:152px;top:430px;width:936px;height:180px;background:var(--earth-soft);padding:20px 26px}
.booking h2{color:#fff;font-size:17px;font-weight:600;margin-bottom:18px}
.booking-row{display:flex;gap:14px;margin-bottom:14px}
.field{height:32px;background:#fff;font-size:12px;color:var(--muted);display:flex;align-items:center;justify-content:space-between;padding:0 10px}
.field.w1{width:200px}
.booking .btn-book{width:190px;height:32px;background:var(--moss);color:#fff;font-size:14px;font-weight:600;display:flex;align-items:center;justify-content:center}

/* intro */
.intro{padding-top:46px}
.section-title{font-size:30px;font-weight:600;color:var(--ink);padding-bottom:10px;border-bottom:1px solid var(--line)}
.intro-body{display:flex;gap:30px;margin-top:30px}
.video{width:330px;height:200px;background:linear-gradient(135deg,#6b8f5a,#a7c48a 55%,#4d6b8c);position:relative;flex:none}
.video .play{position:absolute;left:50%;top:50%;width:54px;height:54px;margin:-27px 0 0 -27px}
.video .bar{position:absolute;left:0;right:0;bottom:0;height:26px;background:rgba(0,0,0,.7)}
.intro-text{font-size:13px;line-height:1.7;color:#555}
.intro-text p+p{margin-top:10px}
.intro-foot{font-size:13px;line-height:1.7;color:#555;margin-top:16px}

/* cards */
.deals{margin-top:34px}
.block-title{font-size:20px;font-weight:700;color:var(--ink);margin-bottom:16px}
.cards{display:flex;gap:30px}
.card{width:306px;border:1px solid var(--line);background:#fff}
.card-photo{height:170px;margin:6px;background:linear-gradient(160deg,#d8cfc2,#b9a992 55%,#8c7a66)}
.card-photo.alt{background:linear-gradient(160deg,#e2ddd4,#c9c2b4 55%,#9d9383)}
.card-photo.ext{background:linear-gradient(180deg,#9cc7e4,#cfe3ee 45%,#9aa98c 70%,#6e8456)}
.card-body{padding:6px 12px 0}
.card h3{font-size:14px;font-weight:700}
.card .date{font-size:12px;color:#555;margin:2px 0 8px}
.card table{width:100%;border-collapse:collapse;font-size:11px;margin-bottom:10px}
.card td{padding:2px 0;color:#666}
.card td.k{color:var(--moss);width:50%}
.card .book{height:32px;background:var(--earth);color:#fff;font-size:12px;font-weight:600;display:flex;align-items:center;justify-content:center;margin:0 6px 6px}
.card .book.hot{background:var(--moss)}

/* bottom trio */
.lower{position:absolute;left:0;top:2090px;width:1200px;height:345px}
.lower-bg{position:absolute;inset:0;background:linear-gradient(180deg,#ffffff 0%,#dfeef5 35%,#bcd9e6 70%,#e8e0cf 100%)}
.trio{display:flex;gap:30px;position:relative;padding-top:20px}
.col{width:306px}
.col h4{font-size:18px;font-weight:700;margin-bottom:12px}
.quote{background:#fff;border:1px solid var(--line);padding:14px 16px;font-size:12px;line-height:1.7;color:#666;font-style:italic;height:150px}
.quote-mark{font-size:40px;color:#bbb;line-height:.6;font-style:normal}
.reviewer{display:flex;align-items:center;gap:12px;margin-top:14px}
.avatar{width:50px;height:50px;border-radius:50%;background:#c9b79c}
.reviewer b{display:block;font-size:12px;color:var(--moss)}
.reviewer span{font-size:11px;color:#777}
.faq-item{height:30px;background:#fff;border:1px solid var(--line);margin-bottom:7px;font-size:12px;color:#555;display:flex;align-items:center;justify-content:space-between;padding:0 12px}
.faq-item.open{background:var(--earth);color:#fff;border-color:var(--earth)}
.faq-panel{background:#fff;border:1px solid var(--line);padding:8px 12px;font-size:11px;color:#777;line-height:1.55;margin:-7px 0 7px}
.news-item{display:flex;gap:12px;margin-bottom:10px;background:#fff;padding:6px}
.news-thumb{width:80px;height:62px;background:linear-gradient(150deg,#8ec3de,#d8c59e);flex:none}
.news-item small{font-size:10px;color:var(--moss)}
.news-item p{font-size:11px;line-height:1.45;color:#555}
.news-item em{font-style:normal;font-size:11px;color:var(--earth);font-weight:600}

/* footer */
.site-footer{position:absolute;left:0;top:2435px;width:1200px;height:335px;background:var(--footer);color:#bbb}
.site-footer .wrap{display:flex;gap:30px;padding-top:24px}
.fcol{width:306px}
.fcol h5{font-size:14px;color:#fff;font-weight:700;padding-bottom:8px;border-bottom:1px solid #444;margin-bottom:12px}
.fcol p{font-size:11px;line-height:1.7}
.subscribe{display:flex;margin-top:12px}
.subscribe span{flex:1;height:28px;background:#fff;font-size:11px;color:#888;display:flex;align-items:center;padding:0 8px}
.subscribe b{width:76px;height:28px;background:var(--moss);color:#fff;font-size:11px;display:flex;align-items:center;justify-content:center}
.fcontact li{list-style:none;font-size:11px;display:flex;gap:8px;align-items:flex-start;margin-bottom:8px;line-height:1.5}
.fsocial{display:flex;gap:6px;justify-content:flex-end;margin-top:14px}
.fsocial i{display:block;width:26px;height:26px;background:var(--moss)}
.copyright{position:absolute;left:0;top:2770px;width:1200px;height:46px;background:var(--footer-deep);font-size:11px;color:#888}
.copyright .wrap{line-height:46px}
</style>
</head>
<body>
<div class="page">

<header class="site-header">
  <div class="wrap">
    <div class="brand"><span class="brand-dot"></span><span class="brand-name">Birchwood Stays</span></div>
    <div class="header-right">
      <div class="header-tools">
        <div class="contact-line">
          <span><svg width="12" height="12" viewBox="0 0 24 24"><path fill="#5b7a3a" d="M6.6 10.8a15 15 0 006.6 6.6l2.2-2.2a1 1 0 011-.25 11 11 0 003.6.6 1 1 0 011 1V20a1 1 0 01-1 1A17 17 0 013 4a1 1 0 011-1h3.5a1 1 0 011 1c0 1.25.2 2.45.6 3.6a1 1 0 01-.25 1z"/></svg>+44 (0)1632 960 418</span>
          <span><svg width="12" height="12" viewBox="0 0 24 24"><path fill="#5b7a3a" d="M2 5h20v14H2zm2 2v.5l8 5 8-5V7z"/></svg>hello@birchwoodstays.com</span>
        </div>
        <div class="socials"><i></i><i></i><i></i><i></i></div>
      </div>
      <div class="site-search"><input value="Search site..." aria-label="Search"><button>Search</button></div>
    </div>
  </div>
</header>

<nav class="main-nav">
  <ul>
    <li class="active">Home</li><li>News</li><li>Reviews</li><li>Caravans &amp; Lodges</li><li>2015 Holidays</li><li>Payment Plans</li><li>Kestrel Bay</li><li>Local Attractions</li>
  </ul>
</nav>

<section class="hero">
  <div class="hero-photo" role="img" aria-label="Family walking on a sunny tropical beach with the sea behind"></div>
  <div class="hero-copy">
    <h1>Let's Discover The<br>World Together</h1>
    <p>Quality Lodge &amp; Caravan Hire at Kestrel Bay Holiday Park. Book online today!</p>
  </div>
  <form class="booking">
    <h2>Where Would you Like To Go ?</h2>
    <div class="booking-row">
      <div class="field w1">Destination city</div>
      <div class="field w1">Check-in</div>
      <div class="field w1">Check-out</div>
      <div class="field w1">Guests</div>
    </div>
    <div class="booking-row">
      <div class="field w1">Adults <span>▾</span></div>
      <div class="field w1">Max Budget <span>▾</span></div>
      <div class="field w1">Bedrooms <span>▾</span></div>
      <div class="btn-book">Book Now</div>
    </div>
  </form>
</section>

<main class="wrap">
  <section class="intro">
    <h2 class="section-title">What Can We Do For You</h2>
    <div class="intro-body">
      <div class="video" role="img" aria-label="Video still of a family outside a holiday caravan">
        <svg class="play" viewBox="0 0 54 54"><circle cx="27" cy="27" r="27" fill="rgba(0,0,0,.6)"/><path d="M21 16l18 11-18 11z" fill="#fff"/></svg>
        <div class="bar"></div>
      </div>
      <div class="intro-text">
        <p>Would you like to book a 2015 caravan or lodge holiday at Kestrel Bay Holiday Park and pay in instalments? You can, with no interest added.</p>
        <p>We have flexible low cost weekly and monthly payment plans available to every guest, starting from a small deposit paid securely by direct debit. This means you can secure your holiday date today without making one large payment, and simply spread the remaining cost over the coming months.</p>
        <p>Once you sign up, the payment plan runs automatically and you will receive a reminder before each collection. You also get the chance to choose which week of the holiday you want and which lodge best suits your family, with the balance cleared before arrival.</p>
      </div>
    </div>
    <p class="intro-foot">If you have any questions about our hassle-free direct debit payment plans please contact us and we will be more than happy to help.</p>
  </section>

  <section class="deals">
    <h3 class="block-title">Late Deals</h3>
    <div class="cards">
      <article class="card">
        <div class="card-photo" role="img" aria-label="Caravan lounge interior"></div>
        <div class="card-body"><h3>The Florida</h3><div class="date">Friday 04 September 2015 (3 nights)</div>
          <table><tr><td class="k">Caravan type</td><td>Gold</td></tr><tr><td class="k">Sleeps</td><td>6</td></tr><tr><td class="k">Bedrooms</td><td>3</td></tr></table></div>
        <div class="book">Book now for £99.00</div>
      </article>
      <article class="card">
        <div class="card-photo alt" role="img" aria-label="Caravan kitchen and dining area"></div>
        <div class="card-body"><h3>The Alberton</h3><div class="date">Friday 04 September 2015 (3 nights)</div>
          <table><tr><td class="k">Caravan type</td><td>Gold</td></tr><tr><td class="k">Sleeps</td><td>6</td></tr><tr><td class="k">Bedrooms</td><td>3</td></tr></table></div>
        <div class="book hot">Book now for £99.00</div>
      </article>
      <article class="card">
        <div class="card-photo" role="img" aria-label="Caravan bedroom interior"></div>
        <div class="card-body"><h3>The Alberton</h3><div class="date">Friday 11 September 2015 (3 nights)</div>
          <table><tr><td class="k">Caravan type</td><td>Silver</td></tr><tr><td class="k">Sleeps</td><td>6</td></tr><tr><td class="k">Bedrooms</td><td>2</td></tr></table></div>
        <div class="book">Book now for £99.00</div>
      </article>
    </div>
  </section>

  <section class="deals">
    <h3 class="block-title">Caravans and lodges</h3>
    <div class="cards">
      <article class="card">
        <div class="card-photo ext" role="img" aria-label="Holiday caravan exterior with decking"></div>
        <div class="card-body"><h3>The Florida</h3><div class="date">Friday 04 September 2015 (3 nights)</div>
          <table><tr><td class="k">Caravan type</td><td>Gold</td></tr><tr><td class="k">Sleeps</td><td>6</td></tr><tr><td class="k">Bedrooms</td><td>3</td></tr></table></div>
        <div class="book">Book now for £99.00</div>
      </article>
      <article class="card">
        <div class="card-photo ext" role="img" aria-label="Lodge exterior on a sunny day"></div>
        <div class="card-body"><h3>The Florida</h3><div class="date">Friday 04 September 2015 (3 nights)</div>
          <table><tr><td class="k">Caravan type</td><td>Gold</td></tr><tr><td class="k">Sleeps</td><td>6</td></tr><tr><td class="k">Bedrooms</td><td>3</td></tr></table></div>
        <div class="book hot">Book now for £99.00</div>
      </article>
      <article class="card">
        <div class="card-photo alt" role="img" aria-label="Lodge lounge interior"></div>
        <div class="card-body"><h3>The Florida</h3><div class="date">Friday 04 September 2015 (3 nights)</div>
          <table><tr><td class="k">Caravan type</td><td>Gold</td></tr><tr><td class="k">Sleeps</td><td>6</td></tr><tr><td class="k">Bedrooms</td><td>3</td></tr></table></div>
        <div class="book">Book now for £99.00</div>
      </article>
    </div>
  </section>
</main>

<section class="lower">
  <div class="lower-bg" role="img" aria-label="Soft beach and caravan scene in the background"></div>
  <div class="wrap trio">
    <div class="col">
      <h4>Testimonials</h4>
      <div class="quote"><div class="quote-mark">“</div>We had a wonderful week in a lovely clean lodge. The children loved the pool and the beach, and booking was easy from start to finish. We will be back next summer.</div>
      <div class="reviewer"><span class="avatar" role="img" aria-label="Guest portrait"></span><div><b>Anna Rowland</b><span>Family guest, 2015</span></div></div>
    </div>
    <div class="col">
      <h4>FAQ</h4>
      <div class="faq-item open">How do payment plans work? <span>▴</span></div>
      <div class="faq-panel">Pay a small deposit, then spread the rest weekly or monthly before your stay.</div>
      <div class="faq-item">Can I bring my dog? <span>▾</span></div>
      <div class="faq-item">What time is check-in? <span>▾</span></div>
      <div class="faq-item">Is bedding included? <span>▾</span></div>
      <div class="faq-item">Can I change my dates? <span>▾</span></div>
    </div>
    <div class="col">
      <h4>Latest News</h4>
      <div class="news-item"><div class="news-thumb" role="img" aria-label="Family on the beach"></div><div><small>August 18, 2015</small><p>New lodges open for the autumn season with sea views.</p><em>Learn More »</em></div></div>
      <div class="news-item"><div class="news-thumb" role="img" aria-label="Children playing by the sea"></div><div><small>August 12, 2015</small><p>Half term family breaks now available to book online.</p><em>Learn More »</em></div></div>
      <div class="news-item"><div class="news-thumb" role="img" aria-label="Park entertainment area"></div><div><small>August 05, 2015</small><p>Summer events programme announced at the park.</p><em>Learn More »</em></div></div>
    </div>
  </div>
</section>

<footer class="site-footer">
  <div class="wrap">
    <div class="fcol">
      <h5>About Us</h5>
      <p>Birchwood Stays offers quality caravan and lodge holidays at Kestrel Bay Holiday Park. We are a friendly family business helping guests find the perfect break by the coast, with flexible payment plans and late deals all year round.</p>
    </div>
    <div class="fcol">
      <h5>Newsletter</h5>
      <p>Subscribe to our newsletter to receive news and updates. We promise not to send you any spam.</p>
      <div class="subscribe"><span>Email address</span><b>Subscribe</b></div>
    </div>
    <div class="fcol">
      <h5>Contact Us</h5>
      <ul class="fcontact">
        <li><svg width="12" height="14" viewBox="0 0 24 28"><path fill="#8fae6a" d="M12 0a9 9 0 00-9 9c0 7 9 19 9 19s9-12 9-19a9 9 0 00-9-9zm0 12a3 3 0 110-6 3 3 0 010 6z"/></svg>14 Kestrel Lane, Alnmoor NE71 4QB</li>
        <li><svg width="12" height="12" viewBox="0 0 24 24"><path fill="#8fae6a" d="M6.6 10.8a15 15 0 006.6 6.6l2.2-2.2a1 1 0 011-.25 11 11 0 003.6.6 1 1 0 011 1V20a1 1 0 01-1 1A17 17 0 013 4a1 1 0 011-1h3.5a1 1 0 011 1c0 1.25.2 2.45.6 3.6a1 1 0 01-.25 1z"/></svg>+44 (0)1632 960 418</li>
        <li><svg width="12" height="12" viewBox="0 0 24 24"><path fill="#8fae6a" d="M2 5h20v14H2zm2 2v.5l8 5 8-5V7z"/></svg>hello@birchwoodstays.com</li>
      </ul>
      <div class="fsocial"><i></i><i></i><i></i></div>
    </div>
  </div>
</footer>
<div class="copyright"><div class="wrap">Copyright © 2015 Birchwood Stays. All rights reserved.</div></div>

</div>
</body>
</html>
```